Stationary & Business Card design for Solo Law Firm
stationary and business card design
Stationary & Business Card design for Solo Law Firm - Law
Creative Brief
Professional
Mira Dalton
Attorney at Law
317 W. Halverd Street, Suite 508 Brookmere, CO 80412
miradalton@kestrelpointlegal.example
kestrelpointlegal.example
underneath my logo I want the following to appear Family Law - Business - Trust & Estates (the spacing or symbol between these terms is up to you)
Logo on the back with the wording above underneath
quillmarsh quillmarsh
#98 can you make the text on the front vertical? and use the back from your #95 with the blue background. I like your submission #72 as well.
#134 can you make the text on the front go vertically instead of horizontally? also can you make the scales on the back bigger?
#141 on the front can you make it vertical? and on the back can you make the logo bigger and put the scales on the back?

```html
<!DOCTYPE html>
<html lang="en">
<head>
<meta charset="utf-8">
<title>Kestrel Point Legal – Business Card</title>
<link rel="stylesheet" href="https://fonts.googleapis.com/css2?family=Cormorant+Garamond:wght@500;600&family=Lato:wght@400;700&display=swap">
<style>
  :root {
    --backdrop: #d9d9d9;
    --rust: #bd5c3c;
    --navy: #2551a3;
    --ink: #3a3a3a;
    --paper: #ffffff;
    --faint: rgba(150, 140, 175, 0.18);
  }
  * { box-sizing: border-box; margin: 0; padding: 0; }
  html, body { width: 1200px; height: 908px; overflow: hidden; }
  body {
    background: var(--backdrop);
    position: relative;
    font-family: "Lato", sans-serif;
  }
  .card {
    position: absolute;
    width: 700px;
    height: 400px;
    border-radius: 26px;
    overflow: hidden;
    box-shadow: 0 10px 26px rgba(0,0,0,0.25);
  }
  /* Back side */
  .card-back {
    left: 70px; top: 50px;
    background: var(--rust);
    color: var(--paper);
  }
  .card-back .emblem-area {
    position: absolute; right: 30px; top: 20px;
    width: 280px; height: 160px;
    border-radius: 20px;
    background: radial-gradient(ellipse at center, rgba(255,255,255,0.12), rgba(255,255,255,0));
  }
  .card-back .firm-name {
    position: absolute; left: 56px; top: 200px;
    font-family: "Cormorant Garamond", serif;
    font-weight: 600;
    font-size: 46px;
    line-height: 56px;
    letter-spacing: 1px;
    text-transform: uppercase;
    white-space: nowrap;
  }
  .card-back .rule {
    position: absolute; left: 56px; top: 268px;
    width: 400px; height: 2px; background: var(--paper);
  }
  .card-back .practice-areas {
    position: absolute; left: 56px; top: 284px;
    font-family: "Cormorant Garamond", serif;
    font-weight: 500;
    font-size: 22px;
    letter-spacing: 1px;
  }
  /* Front side */
  .card-front {
    left: 430px; top: 458px;
    background: var(--paper);
  }
  .card-front .corner-square {
    position: absolute; left: 0; top: 62px;
    width: 44px; height: 44px; background: var(--navy);
  }
  .card-front .emblem-area {
    position: absolute; right: 30px; top: 130px;
    width: 240px; height: 160px;
    border-radius: 20px;
    background: radial-gradient(ellipse at center, var(--faint), rgba(255,255,255,0));
  }
  .card-front .firm-name {
    position: absolute; left: 62px; top: 58px;
    font-family: "Cormorant Garamond", serif;
    font-weight: 600;
    font-size: 38px;
    line-height: 46px;
    color: var(--rust);
    text-transform: uppercase;
    letter-spacing: 1px;
    white-space: nowrap;
  }
  .card-front .name-rule {
    position: absolute; left: 62px; top: 110px;
    width: 300px; height: 2px; background: var(--navy);
  }
  .card-front .accent-bar {
    position: absolute; left: 62px; bottom: 0;
    width: 40px; height: 200px; background: var(--rust);
  }
  .card-front .contact {
    position: absolute; left: 122px; top: 204px;
    list-style: none;
    font-size: 14px; line-height: 22px;
    color: var(--ink);
    white-space: nowrap;
  }
  .card-front .contact li { display: flex; align-items: center; gap: 8px; }
  .card-front .contact svg { width: 14px; height: 14px; flex: none; }
  .card-front .contact .plain { padding-left: 22px; }
  .card-front .identity {
    position: absolute; right: 44px; top: 170px;
    text-align: left;
  }
  .card-front .person {
    font-family: "Cormorant Garamond", serif;
    font-weight: 600; font-size: 30px; line-height: 34px;
    color: var(--navy); text-transform: uppercase;
  }
  .card-front .title {
    font-family: "Cormorant Garamond", serif;
    font-weight: 600; font-size: 19px; line-height: 24px;
    color: var(--rust); text-transform: uppercase; letter-spacing: 1px;
  }
</style>
</head>
<body>
  <section class="card card-back" aria-label="Card back">
    <div class="emblem-area" role="img" aria-label="Faint decorative emblem area"></div>
    <h1 class="firm-name">Kestrel Point Legal</h1>
    <div class="rule"></div>
    <p class="practice-areas">Family Law · Business · Trust &amp; Estates</p>
  </section>

  <section class="card card-front" aria-label="Card front">
    <div class="corner-square"></div>
    <div class="emblem-area" role="img" aria-label="Faint decorative emblem area"></div>
    <h2 class="firm-name">Kestrel Point Legal</h2>
    <div class="name-rule"></div>
    <div class="accent-bar"></div>
    <ul class="contact">
      <li class="plain">317 W. Halverd Street, Suite 508</li>
      <li class="plain">Brookmere, CO 80412</li>
      <li>
        <svg viewBox="0 0 14 14"><circle cx="7" cy="7" r="7" fill="var(--rust)"/><path d="M4.5 3.5l1.5 1.5-1 1c.6 1.3 1.5 2.2 2.8 2.8l1-1 1.5 1.5-1 1c-2.6-.4-4.9-2.7-5.3-5.3z" fill="#fff"/></svg>
        (719) 555-0148
      </li>
      <li>
        <svg viewBox="0 0 14 14"><circle cx="7" cy="7" r="7" fill="var(--rust)"/><rect x="3.5" y="4.5" width="7" height="5" fill="none" stroke="#fff"/><path d="M3.5 4.5L7 7.5l3.5-3" fill="none" stroke="#fff"/></svg>
        miradalton@kestrelpointlegal.example
      </li>
      <li>
        <svg viewBox="0 0 14 14"><circle cx="7" cy="7" r="7" fill="var(--rust)"/><circle cx="7" cy="7" r="3.5" fill="none" stroke="#fff"/><path d="M3.5 7h7M7 3.5v7" stroke="#fff"/></svg>
        kestrelpointlegal.example
      </li>
    </ul>
    <div class="identity">
      <p class="person">Mira Dalton</p>
      <p class="title">Attorney at Law</p>
    </div>
  </section>
</body>
</html>
```